Travel Blogger Business Card for roamquill.net

I need a two-sided business card for a travel blogging website. The card should be both professional and fun at the same time. This is for the website www.roamquill.net

I don't necessarily think that the current logo on the website needs to be used on the business card but it can be. I am very flexible with ideas

Target Market(s)

Travel agencies that will be met at a conference.

Industry/Entity Type

Travel

Contact Information for Business Card

Company Name: Roam Quill.net
Name: Bertrand Olesky
Voice: +1-(345)-402-7731
Address: Coral Reach Shore, Grand Cayman, Cayman Islands
Email: ceo@roamquill.net

Colors
0592cd
0355a3
3176b5
33a6d7
85cae6
85acd3

Requirements
Must have
• Website address and name should be bigger than address, phone number, and email.

```html
<!DOCTYPE html>
<html lang="en">
<head>
<meta charset="utf-8">
<title>Roam Quill.net — Business Card</title>
<link rel="stylesheet" href="https://fonts.googleapis.com/css2?family=Roboto:wght@300;400;700;900&family=Roboto+Condensed:wght@700&display=swap">
<style>
  :root {
    --page-bg: #e9e6e1;
    --blue-deep: #0592cd;
    --blue-bright: #1ec3e3;
    --blue-edge: #0d7fba;
    --accent: #33a6d7;
    --card-dark: #222325;
    --card-dark-2: #2b2c2f;
    --map-tone: #2c3844;
    --text-light: #ffffff;
    --text-soft: #e6e8ea;
  }
  * { box-sizing: border-box; margin: 0; padding: 0; }
  html, body { width: 1200px; height: 1023px; overflow: hidden; }
  body {
    background: var(--page-bg);
    font-family: "Roboto", Arial, sans-serif;
    display: flex;
    flex-direction: column;
    align-items: center;
    justify-content: center;
    gap: 60px;
  }
  .card {
    position: relative;
    width: 700px;
    height: 400px;
    border-radius: 22px;
    overflow: hidden;
    box-shadow: 0 10px 28px rgba(0,0,0,.22);
  }

  /* Front */
  .card--front {
    background: radial-gradient(ellipse 70% 80% at 58% 40%, var(--blue-bright) 0%, #12aedb 45%, var(--blue-deep) 100%);
  }
  .front-brand {
    position: absolute;
    left: 0; right: 0;
    top: 150px;
    display: flex;
    align-items: center;
    justify-content: center;
    gap: 20px;
  }
  .brand-dot {
    width: 46px; height: 46px;
    border-radius: 50%;
    background: var(--text-light);
  }
  .brand-name {
    font-family: "Roboto Condensed", "Arial Narrow", sans-serif;
    font-weight: 700;
    font-size: 68px;
    letter-spacing: -1px;
    color: var(--text-light);
    text-transform: uppercase;
    line-height: 1;
  }
  .front-web {
    position: absolute;
    left: 0; right: 0;
    bottom: 46px;
    text-align: center;
    font-size: 22px;
    color: var(--text-light);
    letter-spacing: .3px;
  }

  /* Back */
  .card--back {
    background: linear-gradient(135deg, var(--card-dark-2), var(--card-dark));
    color: var(--text-soft);
  }
  .back-map {
    position: absolute;
    left: 150px; top: 60px;
    width: 520px; height: 300px;
    border-radius: 40% 50% 45% 40%;
    background: radial-gradient(ellipse at center, var(--map-tone) 0%, rgba(44,56,68,.35) 60%, rgba(44,56,68,0) 100%);
  }
  .person { position: absolute; left: 44px; top: 36px; }
  .person-name {
    font-weight: 300;
    font-size: 34px;
    color: var(--accent);
  }
  .person-role {
    font-size: 15px;
    color: var(--text-light);
    margin-top: 2px;
  }
  .contacts {
    position: absolute;
    left: 44px; top: 128px;
    list-style: none;
    display: flex;
    flex-direction: column;
    gap: 12px;
    font-size: 17px;
  }
  .contacts li { display: flex; align-items: center; gap: 12px; }
  .contacts svg { width: 18px; height: 18px; flex: none; }
  .address {
    position: absolute;
    right: 44px; top: 215px;
    display: flex;
    gap: 14px;
    font-size: 22px;
    line-height: 1.3;
    color: var(--text-light);
  }
  .address svg { width: 20px; height: 26px; flex: none; margin-top: 2px; }
  .back-brand {
    position: absolute;
    left: 44px; bottom: 34px;
    display: flex;
    align-items: center;
    gap: 12px;
  }
  .back-brand .brand-dot { width: 26px; height: 26px; }
  .back-brand .brand-name { font-size: 38px; }
</style>
</head>
<body>

<section class="card card--front" aria-label="Card front">
  <div class="front-brand">
    <span class="brand-dot"></span>
    <span class="brand-name">Roam Quill</span>
  </div>
  <p class="front-web">www.roamquill.net</p>
</section>

<section class="card card--back" aria-label="Card back">
  <div class="back-map" role="img" aria-label="Faint dotted world map in the background"></div>

  <div class="person">
    <p class="person-name">Bertrand Olesky</p>
    <p class="person-role">CEO</p>
  </div>

  <ul class="contacts">
    <li>
      <svg viewBox="0 0 20 20" fill="none" stroke="var(--accent)" stroke-width="1.6"><circle cx="10" cy="10" r="8.5"/><path d="M7 6c0 4 3 7 7 7l.5-1.8-2-1-1 1c-1.3-.6-2.4-1.7-3-3l1-1-1-2z" fill="var(--accent)" stroke="none"/></svg>
      <span>+1-(345)-402-7731</span>
    </li>
    <li>
      <svg viewBox="0 0 20 20" fill="none" stroke="var(--accent)" stroke-width="1.6"><rect x="2" y="4.5" width="16" height="11" rx="1"/><path d="M2 5l8 6 8-6"/></svg>
      <span>ceo@roamquill.net</span>
    </li>
    <li>
      <svg viewBox="0 0 20 20" fill="none" stroke="var(--accent)" stroke-width="1.4"><circle cx="10" cy="10" r="8.5"/><ellipse cx="10" cy="10" rx="4" ry="8.5"/><path d="M1.5 10h17M3 5.5h14M3 14.5h14"/></svg>
      <span>www.roamquill.net</span>
    </li>
  </ul>

  <div class="address">
    <svg viewBox="0 0 20 26"><path d="M10 1C5 1 1.5 4.6 1.5 9.3 1.5 15.5 10 25 10 25s8.5-9.5 8.5-15.7C18.5 4.6 15 1 10 1z" fill="var(--accent)"/><circle cx="10" cy="9.5" r="3.3" fill="var(--card-dark)"/></svg>
    <p>Coral Reach Shore, Grand<br>Cayman, Cayman Islands</p>
  </div>

  <div class="back-brand">
    <span class="brand-dot"></span>
    <span class="brand-name">Roam Quill</span>
  </div>
</section>

</body>
</html>
```